Business Card Design for a Sound engineer and DJ

We would like a residn of the business card.

Logo must remain the same.
The card is for the owner of the company.
The business card is in Arabic as the company is based in Kuwait.
The company specializes in sound engineering for singers concerts and events and in addition DJ.
The color options is up to the designer but we would like it masculine as the owner is a man.

Target Market(s)

All ages

Industry/Entity Type

Media

Contact Information for Business Card

Name:
Eng. Tarek Halabi
م/طارق حلبي

The name above is in Arabic and English.

Title: General Manager
Mobile: +965 66307852
Office: +965 22486037
Email: info@sawtarin.net

Address:
Office no. 3
1st floor
Almarfa Complex
Rashed AlQeblawi St.
Salmiya
Kuwait

Instagram: @sawtarin
Snap: sawtarin

Requirements
Nice to have
• can we have Instagram icon and snap icon and a phone vector and email?
• Instead of writing the words

```html
<!DOCTYPE html>
<html lang="en">
<head>
<meta charset="utf-8">
<title>Sawtarin — Business Card</title>
<link rel="stylesheet" href="https://fonts.googleapis.com/css2?family=Open+Sans:wght@400;600;700&family=Noto+Kufi+Arabic:wght@400;600&display=swap">
<style>
  :root {
    --bg: #000000;
    --panel: #030303;
    --ink: #ffffff;
    --ink-soft: #d9d9e3;
    --accent: #6a72b6;
    --brand: #8b4fa5;
    --brand-soft: #9466b0;
  }
  html, body {
    margin: 0;
    padding: 0;
    width: 1200px;
    height: 685px;
    overflow: hidden;
    background: var(--bg);
  }
  .card {
    position: relative;
    width: 1200px;
    height: 685px;
    background: var(--bg);
    font-family: "Open Sans", sans-serif;
    color: var(--ink);
  }
  .brand-panel {
    position: absolute;
    left: 0;
    top: 64px;
    width: 565px;
    height: 578px;
    background: var(--panel);
  }
  .brand-mark {
    position: absolute;
    left: 221px;
    top: 222px;
    width: 120px;
    height: 120px;
    border-radius: 50%;
    background: var(--brand);
  }
  .brand-name {
    position: absolute;
    left: 140px;
    top: 404px;
    width: 290px;
    text-align: center;
    font-size: 34px;
    font-weight: 600;
    letter-spacing: 7px;
    color: var(--brand);
    margin: 0;
    line-height: 1;
    text-transform: uppercase;
  }
  .brand-tagline {
    position: absolute;
    left: 140px;
    top: 448px;
    width: 290px;
    text-align: center;
    margin: 0;
    font-size: 16.5px;
    font-weight: 700;
    letter-spacing: 1px;
    color: var(--brand-soft);
    line-height: 1;
  }
  .brand-tagline-ar {
    position: absolute;
    left: 140px;
    top: 468px;
    width: 290px;
    text-align: center;
    margin: 0;
    font-family: "Noto Kufi Arabic", sans-serif;
    font-size: 16px;
    font-weight: 600;
    color: var(--brand-soft);
    direction: rtl;
  }
  .holder {
    position: absolute;
    left: 801px;
    top: 138px;
  }
  .holder-name-ar {
    margin: 0;
    font-family: "Noto Kufi Arabic", sans-serif;
    font-size: 17px;
    font-weight: 400;
    color: var(--ink-soft);
    line-height: 1.3;
    direction: rtl;
    text-align: left;
  }
  .holder-name {
    margin: 2px 0 0;
    font-size: 25px;
    font-weight: 400;
    letter-spacing: 1.5px;
    line-height: 1.3;
  }
  .holder-name .prefix { color: var(--ink-soft); }
  .holder-title {
    margin: 10px 0 0;
    font-size: 19px;
    font-weight: 700;
    letter-spacing: 2.6px;
    color: var(--accent);
    text-transform: uppercase;
  }
  .contact-row {
    position: absolute;
    left: 801px;
    display: flex;
    align-items: center;
  }
  .contact-row .icon { flex: none; }
  .contact-row .value {
    font-size: 24px;
    letter-spacing: 2.4px;
  }
  .row-mobile { top: 328px; }
  .row-office { top: 396px; }
  .row-mobile .value { margin-left: 24px; }
  .row-office .value { margin-left: 20px; }
  .row-social { top: 460px; }
  .social-dot {
    width: 50px;
    height: 50px;
    border-radius: 50%;
    background: var(--accent);
  }
  .row-social .value {
    margin-left: 55px;
    font-size: 19px;
    letter-spacing: 3.5px;
    text-transform: uppercase;
  }
  .row-email { top: 536px; }
  .row-email .value {
    font-size: 20px;
    letter-spacing: 3.6px;
    text-transform: uppercase;
  }
</style>
</head>
<body>
<main class="card">
  <section class="brand-panel" aria-label="Brand">
    <div class="brand-mark" aria-hidden="true"></div>
    <h1 class="brand-name">Sawtarin</h1>
    <p class="brand-tagline">DJ - SOUND ENG. - LIGHTING</p>
    <p class="brand-tagline-ar">دي جي - هندسة صوت - إضاءة</p>
  </section>

  <section class="holder" aria-label="Card holder">
    <p class="holder-name-ar">م/طارق حلبي</p>
    <p class="holder-name"><span class="prefix">ENG.\ </span>Tarek Halabi</p>
    <p class="holder-title">General Manager</p>
  </section>

  <div class="contact-row row-mobile">
    <svg class="icon" width="26" height="48" viewBox="0 0 26 48" aria-label="Mobile">
      <rect x="1.5" y="1.5" width="23" height="45" rx="4" fill="none" stroke="var(--accent)" stroke-width="3"/>
      <rect x="5" y="8" width="16" height="30" fill="var(--accent)"/>
      <circle cx="13" cy="42" r="1.6" fill="var(--accent)"/>
    </svg>
    <span class="value">+965 66307852</span>
  </div>

  <div class="contact-row row-office">
    <svg class="icon" width="46" height="36" viewBox="0 0 46 36" aria-label="Office phone">
      <rect x="0" y="2" width="10" height="34" rx="3" fill="var(--accent)"/>
      <rect x="12" y="6" width="34" height="30" rx="3" fill="var(--accent)"/>
      <rect x="16" y="0" width="24" height="6" fill="var(--accent)"/>
      <g fill="#000">
        <rect x="17" y="10" width="24" height="6"/>
        <rect x="18" y="20" width="4" height="3"/><rect x="27" y="20" width="4" height="3"/><rect x="36" y="20" width="4" height="3"/>
        <rect x="18" y="25" width="4" height="3"/><rect x="27" y="25" width="4" height="3"/><rect x="36" y="25" width="4" height="3"/>
        <rect x="18" y="30" width="4" height="3"/><rect x="27" y="30" width="4" height="3"/><rect x="36" y="30" width="4" height="3"/>
      </g>
    </svg>
    <span class="value">+965 22486037</span>
  </div>

  <div class="contact-row row-social">
    <div class="social-dot" aria-hidden="true"></div>
    <span class="value">sawtarin</span>
  </div>

  <div class="contact-row row-email">
    <span class="value">info@sawtarin.net</span>
  </div>
</main>
</body>
</html>
```